GP Information brochure

we are looking for a designed brochure to send to doctors regarding our products and services. i have attached a very brief design and some information to start the design process.
I have also attached a previous flyer so that the theme and designs stay the same
please let me know if you require anything further
our slogan is: "Improving the quality of life for every individual"
Size: A4
Target Market(s)
general practitioners and allied health industry
Industry/Entity Type
Health And Wellness
Look and feel

```html
<!DOCTYPE html>
<html lang="en">
<head>
<meta charset="utf-8">
<title>Movewell Health Club – GP Information</title>
<link rel="stylesheet" href="https://fonts.googleapis.com/css2?family=Roboto+Condensed:wght@700&family=Arimo:wght@400;700&display=swap">
<style>
  :root {
    --orange: #ee8a1c;
    --green: #8cc63f;
    --blue: #2a9fd6;
    --navy: #2b3a8f;
    --text-blue: #3a8fc4;
    --white: #ffffff;
    --paper: #ffffff;
  }
  * { margin: 0; padding: 0; box-sizing: border-box; }
  html, body { width: 848px; height: 1200px; overflow: hidden; background: var(--paper); }
  .flyer { position: relative; width: 848px; height: 1200px; overflow: hidden; background: var(--paper); font-family: "Arimo", Arial, sans-serif; }
  .backdrop { position: absolute; inset: 0; }
  .gym-photo { position: absolute; left: 0; top: 150px; width: 470px; height: 760px;
    background: radial-gradient(ellipse at 55% 45%, rgba(210,214,220,0.55), rgba(235,238,242,0.35) 55%, rgba(255,255,255,0) 80%); }
  .brand { position: absolute; left: 386px; top: 52px; display: flex; align-items: center; gap: 18px; }
  .brand-dot { width: 94px; height: 94px; border-radius: 50%; background: var(--navy); }
  .brand-text { display: flex; flex-direction: column; }
  .brand-name { font-family: "Roboto Condensed", "Arial Narrow", sans-serif; font-weight: 700; font-size: 64px; line-height: 1; color: var(--navy); letter-spacing: 3px; }
  .brand-sub { margin-top: 6px; background: var(--orange); color: var(--white); font-family: "Roboto Condensed", sans-serif; font-weight: 700; font-size: 15px; text-align: center; padding: 2px 0; width: 286px; letter-spacing: 1px; }
  .slogan { position: absolute; left: 51px; top: 232px; font-family: "Roboto Condensed", "Arial Narrow", sans-serif; font-weight: 700; font-size: 58px; line-height: 52px; color: var(--orange); text-transform: uppercase; }
  .intro { position: absolute; left: 57px; top: 516px; width: 342px; font-size: 14.6px; line-height: 21px; color: var(--text-blue); }
  .intro p + p { margin-top: 21px; }
  .intro .name { color: var(--orange); font-weight: 700; }
  .photo-round { position: absolute; border-radius: 50%; border: 7px solid var(--white); box-shadow: 0 4px 14px rgba(0,0,0,0.18); }
  .photo-cardio { left: 463px; top: 229px; width: 394px; height: 394px;
    background: radial-gradient(circle at 40% 45%, #b78a86, #7a6a78 40%, #4f5a6e 70%, #c9c2b6); }
  .photo-team { left: 410px; top: 622px; width: 320px; height: 320px;
    background: radial-gradient(circle at 50% 50%, #e4d2b8, #9ec9ea 35%, #5aa6de 75%, #3f8fcf); }
  .photo-trainers { position: absolute; left: 28px; top: 872px; width: 302px; height: 328px;
    background: radial-gradient(ellipse at 50% 45%, #8d6f5c, #5b5d63 45%, rgba(120,120,125,0.6) 70%, rgba(255,255,255,0) 85%); }
  .social { position: absolute; left: 402px; top: 1084px; display: flex; gap: 2px; }
  .social span { width: 32px; height: 32px; border-radius: 50%; background: var(--green); }
  .contact { position: absolute; left: 603px; top: 995px; color: var(--white); font-style: normal; }
  .contact h2 { font-size: 16.5px; line-height: 19px; font-weight: 700; margin-left: 21px; margin-bottom: 4px; }
  .contact ul { list-style: none; }
  .contact li { display: flex; align-items: flex-start; gap: 5px; font-size: 14.6px; line-height: 19px; margin-bottom: 6px; }
  .contact svg { flex: 0 0 16px; width: 16px; height: 18px; margin-top: 1px; }
</style>
</head>
<body>
<main class="flyer">
  <div class="gym-photo" role="img" aria-label="Faded photo of a modern gym interior"></div>

  <svg class="backdrop" width="848" height="1200" viewBox="0 0 848 1200" aria-hidden="true">
    <path d="M0 47 C220 74 420 140 568 256 C410 168 210 112 0 72 Z" fill="var(--orange)"/>
    <path d="M0 112 C220 134 420 196 560 272 C410 214 210 164 0 134 Z" fill="var(--green)"/>
    <path d="M0 1108 C300 1018 620 840 848 565 L848 595 C620 868 300 1050 0 1142 Z" fill="var(--green)"/>
    <path d="M0 1178 C310 1076 640 890 848 625 L848 1200 L0 1200 Z" fill="var(--blue)"/>
    <path d="M0 1166 C310 1064 640 878 848 615 L848 625 C640 890 310 1076 0 1178 Z" fill="var(--white)"/>
  </svg>

  <header class="brand">
    <span class="brand-dot"></span>
    <div class="brand-text">
      <span class="brand-name">movewell</span>
      <span class="brand-sub">HEALTH CLUB</span>
    </div>
  </header>

  <h1 class="slogan">Improving<br>the quality<br>of life<br>for every<br>individual</h1>

  <section class="intro">
    <p><span class="name">Movewell</span> has a well-equipped and modern 24/7 training facility in Westmere, southern suburb of Sydney. In addition they have the capability to bring structured health and well being programs to any area of Australia.</p>
    <p>Marcus, along with being an Exercise Physiologist, has built and works along side a strong network of allied health professional enabling them to call on a wide range of services including dietitians, physiotherapist and strength and condition. Movewell has the capability to provide a wide range of professionally design programs for wide demographics with the most recent knowledge and methods.</p>
  </section>

  <div class="photo-round photo-cardio" role="img" aria-label="Photo of smiling older women on cross-trainers with a personal trainer"></div>
  <div class="photo-round photo-team" role="img" aria-label="Photo of hands reaching towards a ball against a blue sky"></div>
  <div class="photo-trainers" role="img" aria-label="Photo of a male and female trainer holding dumbbells"></div>

  <div class="social" aria-label="Social media">
    <span></span><span></span><span></span><span></span><span></span>
  </div>

  <address class="contact">
    <h2>Movewell<br>Health Club</h2>
    <ul>
      <li>
        <svg viewBox="0 0 16 18"><path d="M8 1a5.5 5.5 0 0 0-5.5 5.5C2.5 11 8 17 8 17s5.5-6 5.5-10.5A5.5 5.5 0 0 0 8 1zm0 7.5a2 2 0 1 1 0-4 2 2 0 0 1 0 4z" fill="var(--green)"/></svg>
        <span>27, Harbour Ridge Road,<br>Westmere, Sydney<br>NSW 2231</span>
      </li>
      <li>
        <svg viewBox="0 0 16 18"><path d="M3.5 2.5l2.5-.5 1.5 3.5-1.8 1.2a8 8 0 0 0 3.6 3.6l1.2-1.8 3.5 1.5-.5 2.5c-.3.8-1 1.2-1.8 1.1C6.8 13 3.2 9.4 2.4 4.3c-.1-.8.3-1.5 1.1-1.8z" fill="var(--green)"/></svg>
        <span>612 80001234</span>
      </li>
      <li>
        <svg viewBox="0 0 16 18"><rect x="1" y="4" width="14" height="10" fill="var(--green)"/><path d="M1 4l7 6 7-6" fill="none" stroke="var(--blue)" stroke-width="1.4"/></svg>
        <span>admin@movewell.club</span>
      </li>
      <li>
        <svg viewBox="0 0 16 18"><circle cx="8" cy="9" r="6.5" fill="none" stroke="var(--green)" stroke-width="1.5"/><ellipse cx="8" cy="9" rx="2.8" ry="6.5" fill="none" stroke="var(--green)" stroke-width="1.3"/><path d="M1.5 9h13M2.5 5.8h11M2.5 12.2h11" stroke="var(--green)" stroke-width="1.2"/></svg>
        <span>www.movewell.club</span>
      </li>
    </ul>
  </address>
</main>
</body>
</html>
```